Innovative Healthcare Technology Company needs a Business Card Design

We are in need of an innovative business card design for a new healthcare software company called "Brightwell Harbor Systems". We develop software that creates medical assessment applications and mobile e-learning prevention services to reduce risk behaviors in adolescent and young adults. Our initial product, the "MERIDIAN App", conducts a tailored sexual risk assessment and provides a doctor with an insightful patient report to improve sexual risk counseling and ultimately reduce unintended pregnancy, STDs, etc.

We would like the design to incorporate our logo and branding colors (attached) in an innovative and creative manner. The final design should communicate professionalism and healthcare innovation. Our tag line is "prevention is the solution" (doesn't necessarily need to be included) and our target audience is doctors, medical directors, and medical business administrators. Please visit our website for additional info ourlantrixhub.com. Be creative and we look forward to seeing your designs!

Target Market(s)

healthcare - doctors, medical directors and medical business administrators

Industry/Entity Type

Healthcare

Contact Information for Business Card

We would like the design to incorporate our logo and branding colors (attached) in an innovative and creative manner. The final design should communicate professionalism and healthcare innovation. Our tag line is "prevention is the solution" (doesn't necessarily need to be included)

Font styles to use
Other font styles liked:
• quicksand

Requirements
Must have
• our logo and brand colors
• Name, (Joan Ferraventi, PhD)
• Email (drjoan@ourlantrixhub.com)
• phone (555.213.8870)
• Website (ourlantrixhub.com)
Should not have
• cartoon look

```html
<!DOCTYPE html>
<html lang="en">
<head>
<meta charset="utf-8">
<title>Brightwell Harbor Systems — Business Card</title>
<link rel="stylesheet" href="https://fonts.googleapis.com/css2?family=Quicksand:wght@400;500;700&display=swap">
<style>
  :root {
    --page-bg: #d9dcdf;
    --card-bg: #eef1f3;
    --card-edge: #9aa2a8;
    --navy: #1f3a63;
    --slate: #6e7378;
    --rule-gray: #7d8186;
    --brand-green: #3f7a5c;
    --visual-a: #dfe5ea;
    --visual-b: #c9d3db;
  }
  * { margin: 0; padding: 0; box-sizing: border-box; }
  html, body {
    width: 1200px;
    height: 970px;
    overflow: hidden;
    background: var(--page-bg);
    font-family: "Quicksand", sans-serif;
  }
  .business-card {
    position: absolute;
    left: 80px;
    top: 196px;
    width: 1040px;
    height: 578px;
    background: var(--card-bg);
    border: 1px solid var(--card-edge);
    overflow: hidden;
  }
  .card-visual {
    position: absolute;
    left: 260px;
    top: 70px;
    width: 780px;
    height: 508px;
    background: radial-gradient(ellipse at 55% 55%, var(--visual-b) 0%, var(--visual-a) 55%, rgba(238,241,243,0) 80%);
    opacity: 0.8;
  }
  .brand {
    position: absolute;
    left: 52px;
    top: 58px;
    display: flex;
    align-items: center;
    gap: 18px;
  }
  .brand-mark {
    width: 34px;
    height: 34px;
    background: var(--brand-green);
  }
  .brand-name {
    font-weight: 500;
    font-size: 44px;
    color: var(--navy);
    line-height: 1;
    letter-spacing: 0.5px;
  }
  .holder {
    position: absolute;
    right: 52px;
    top: 300px;
    font-size: 30px;
    color: var(--navy);
    letter-spacing: 1px;
  }
  .holder-name { font-weight: 700; }
  .holder-title { font-weight: 400; }
  .rule-thin {
    position: absolute;
    left: 50px;
    top: 355px;
    width: 530px;
    height: 1px;
    background: var(--rule-gray);
  }
  .rule-accent {
    position: absolute;
    left: 580px;
    top: 353px;
    width: 410px;
    height: 3px;
    background: var(--navy);
  }
  .contact-list {
    position: absolute;
    left: 50px;
    top: 405px;
    list-style: none;
  }
  .contact-item {
    display: flex;
    align-items: center;
    gap: 12px;
    height: 42px;
    font-size: 23px;
    font-weight: 500;
    color: var(--slate);
    letter-spacing: 1px;
  }
  .contact-icon { width: 24px; height: 24px; flex: none; }
</style>
</head>
<body>
  <div class="business-card">
    <div class="card-visual" role="img" aria-label="Faint photo of hands holding a tablet beside a stethoscope"></div>

    <div class="brand">
      <div class="brand-mark"></div>
      <div class="brand-name">Brightwell Harbor Systems</div>
    </div>

    <div class="holder"><span class="holder-name">Joan Ferraventi</span><span class="holder-title">, PhD</span></div>
    <div class="rule-thin"></div>
    <div class="rule-accent"></div>

    <ul class="contact-list">
      <li class="contact-item">
        <svg class="contact-icon" viewBox="0 0 24 24" aria-hidden="true">
          <path d="M6.6 3.5l2.6 3.4-1.6 2.2c1.2 2.5 3 4.4 5.4 5.6l2.2-1.6 3.4 2.6-1.4 3.3c-7.4-.6-12.7-5.9-13.2-13.2z" fill="var(--navy)"/>
          <path d="M14 4.5a6 6 0 0 1 5.5 5.5M14 7.5a3 3 0 0 1 2.5 2.5" stroke="var(--navy)" stroke-width="1.5" fill="none"/>
        </svg>
        <span>555.213.8870</span>
      </li>
      <li class="contact-item">
        <svg class="contact-icon" viewBox="0 0 24 24" aria-hidden="true">
          <rect x="2.5" y="5.5" width="19" height="13" fill="var(--navy)"/>
          <path d="M3 6.5l9 6.5 9-6.5" stroke="var(--card-bg)" stroke-width="1.5" fill="none"/>
        </svg>
        <span>drjoan@ourlantrixhub.com</span>
      </li>
      <li class="contact-item">
        <svg class="contact-icon" viewBox="0 0 24 24" aria-hidden="true">
          <circle cx="12" cy="12" r="9" fill="none" stroke="var(--navy)" stroke-width="2"/>
          <path d="M3 12h18M12 3c3 3 3 15 0 18M12 3c-3 3-3 15 0 18" stroke="var(--navy)" stroke-width="1.5" fill="none"/>
        </svg>
        <span>ourlantrixhub.com</span>
      </li>
    </ul>
  </div>
</body>
</html>
```